Task Scheduling Web App

I have a basic web app that I need designed. It must be mobile-first but it needs to be responsive for desktop users as well.
1. Before beginning the exercise, the user inputs basic info on their country and age.
2. The user is then presented with two piles of cards (TASK or DAY), with the top card face up. They have 20 seconds before their combination is set, during which they can replace either of the cards at random as many times as they like. At any time they find a combination they’re happy with, they can progress to the next screen. If the clock runs out the combination is set based on whatever cards are showing at the time and they’re moved on to the next screen.
3. The user is presented with a blank graph; x axis is ‘How important is it?’, y axis is ‘How often does it need to be done?’. The two cards they picked in the previous screen are combined to create a COMBO and the user must place a mark somewhere on the graph to represent how important they believe the scheduled task to be vs how often it will need to be done.
4. Once the user has picked a spot on the graph, options appear for them to re-do the exercise by choosing a new combo or to progress and see how their peers are organising their tasks.
5. If they choose to view insights, they must login with Quelvorn so a popup will appear to facilitate this.
6. After logging in with Quelvorn, users can view the top 10 combinations for their demographic listed and mapped on a graph. This information is based on the selection and ranking of combinations by other users.

```html
<!DOCTYPE html>
<html lang="en">
<head>
<meta charset="utf-8">
<title>Tallyvane Pair – App Screens</title>
<link rel="stylesheet" href="https://fonts.googleapis.com/css2?family=Roboto:wght@400;500;700&display=swap">
<style>
  :root {
    --canvas: #cbcccd;
    --status: #0b5e5f;
    --appbar: #9c130f;
    --navbar: #000000;
    --white: #ffffff;
    --field-line: rgba(255,255,255,0.85);
    --insights-fill: rgba(236,190,188,0.8);
    --go-start: #4a0f2f;
    --go-end: #a8140e;
    --axis: rgba(255,255,255,0.75);
  }
  html, body { margin: 0; padding: 0; }
  body {
    width: 1200px; height: 836px; overflow: hidden;
    background: var(--canvas);
    font-family: "Roboto", sans-serif;
  }
  .stage {
    width: 1436px; height: 1000px; position: relative;
    transform: scale(0.8357); transform-origin: 0 0;
  }
  .phone {
    position: absolute; top: 180px; width: 360px; height: 640px;
    overflow: hidden; color: var(--white);
  }
  .phone--login { left: 70px; }
  .phone--info { left: 450px; }
  .phone--chart { left: 830px; }

  .backdrop { position: absolute; inset: 0; }
  .phone--login .backdrop {
    background:
      radial-gradient(ellipse 60% 45% at 50% 60%, rgba(214,80,60,0.55), transparent 70%),
      linear-gradient(160deg, #8f2127 0%, #a7302d 45%, #8a2a33 100%);
  }
  .phone--info .backdrop, .phone--chart .backdrop {
    background:
      radial-gradient(ellipse 45% 50% at 45% 55%, rgba(220,80,55,0.75), transparent 75%),
      radial-gradient(ellipse 40% 30% at 80% 20%, rgba(120,20,70,0.6), transparent 70%),
      linear-gradient(135deg, #5a1733 0%, #7a1f2a 40%, #b43a2c 70%, #3a2a3c 100%);
  }

  .status-bar {
    position: absolute; top: 0; left: 0; right: 0; height: 25px;
    background: var(--status);
    display: flex; justify-content: flex-end; align-items: center;
    gap: 5px; padding-right: 8px; box-sizing: border-box;
    font-size: 14px; font-weight: 500;
  }
  .app-bar {
    position: absolute; top: 25px; left: 0; right: 0; height: 43px;
    background: var(--appbar);
    display: flex; align-items: center; justify-content: center;
    font-size: 18px; letter-spacing: 0.3px;
  }
  .app-bar .back { position: absolute; left: 17px; top: 15px; }
  .app-bar .menu { position: absolute; right: 14px; top: 12px; }
  .nav-bar {
    position: absolute; bottom: 0; left: 0; right: 0; height: 48px;
    background: var(--navbar);
  }
  .nav-bar svg { position: absolute; top: 14px; }

  .app-name {
    position: absolute; top: 108px; left: 0; right: 0; margin: 0;
    text-align: center; font-weight: 400; line-height: 1;
  }
  .app-name .line-1 { display: block; font-size: 38px; }
  .app-name .line-2 { display: block; font-size: 46px; margin-top: 8px; }

  .provider-name {
    position: absolute; top: 310px; left: 0; right: 0; text-align: center;
    font-size: 36px; font-weight: 700;
  }

  .field, .button {
    position: absolute; left: 29px; width: 304px; height: 51px;
    box-sizing: border-box; border: 1px solid var(--field-line);
    display: flex; align-items: center; font-size: 17px;
  }
  .field { padding-left: 13px; }
  .row-1 { top: 368px; } .row-2 { top: 428px; } .row-3 { top: 488px; }
  .field .caret {
    position: absolute; right: 0; top: 0; bottom: 0; width: 42px;
    background: rgba(255,255,255,0.3);
    display: flex; align-items: center; justify-content: center; font-size: 14px;
  }
  .button { justify-content: center; font-weight: 500; }
  .button--insights { background: var(--insights-fill); color: #2a1518; font-weight: 400; }
  .button--go { background: linear-gradient(90deg, var(--go-start), var(--go-end)); font-size: 16px; }
  .forgot { position: absolute; top: 549px; left: 0; right: 0; text-align: center; font-size: 14px; }

  .chart { position: absolute; top: 100px; left: 0; width: 360px; height: 250px; }
  .chart-label { position: absolute; font-size: 11px; }
  .axis-title { position: absolute; font-size: 14px; }
  .axis-title--y { left: 21px; top: 265px; transform: rotate(-90deg); transform-origin: 0 0; white-space: nowrap; }

  .pick { width: 147px; font-weight: 400; font-size: 17px; }
  .pick--day { left: 185px; }
  .combo { font-size: 24px; font-weight: 500; }
  .action {
    width: 147px; height: 71px; font-size: 15px; line-height: 18px; text-align: center;
    background: linear-gradient(90deg, var(--go-start), var(--go-end));
  }
  .action--peers { left: 185px; }
</style>
</head>
<body>
<div class="stage">

  <!-- Login screen -->
  <section class="phone phone--login">
    <div class="backdrop" role="img" aria-label="Warm red textured background with faint concentric rings"></div>
    <div class="status-bar">
      <svg width="16" height="16" viewBox="0 0 16 16"><circle cx="8" cy="9" r="5.5" fill="none" stroke="#fff" stroke-width="1.8"/><path d="M8 6v3l2 1" stroke="#fff" stroke-width="1.5" fill="none"/></svg>
      <svg width="20" height="14" viewBox="0 0 20 14"><path d="M0 3Q10-3 20 3L10 14Z" fill="#fff"/></svg>
      <svg width="14" height="14" viewBox="0 0 14 14"><path d="M0 14L14 0V14Z" fill="#fff"/></svg>
      <svg width="8" height="14" viewBox="0 0 8 14"><rect x="0.5" y="1.5" width="7" height="12" fill="none" stroke="#fff"/><rect x="2.5" y="0" width="3" height="2" fill="#fff"/><rect x="1.5" y="8" width="5" height="5" fill="#fff"/></svg>
      <span>16:54</span>
    </div>
    <h1 class="app-name"><span class="line-1">TALLYVANE</span><span class="line-2">PAIR</span></h1>
    <div class="provider-name">Quelvorn</div>
    <div class="field row-1">Email</div>
    <div class="field row-2">Password</div>
    <div class="button button--insights row-3">GET INSIGHTS</div>
    <div class="forgot">Forgot Password?</div>
    <nav class="nav-bar">
      <svg style="left:72px" width="18" height="20" viewBox="0 0 18 20"><path d="M16 1L2 10L16 19Z" fill="none" stroke="#fff" stroke-width="1.8"/></svg>
      <svg style="left:170px" width="20" height="20" viewBox="0 0 20 20"><circle cx="10" cy="10" r="8.5" fill="none" stroke="#fff" stroke-width="1.8"/></svg>
      <svg style="left:272px" width="16" height="20" viewBox="0 0 16 20"><rect x="1" y="3" width="14" height="14" fill="none" stroke="#fff" stroke-width="1.8"/></svg>
    </nav>
  </section>

  <!-- User info screen -->
  <section class="phone phone--info">
    <div class="backdrop" role="img" aria-label="Deep red and purple glowing background with faint concentric rings"></div>
    <div class="status-bar">
      <svg width="16" height="16" viewBox="0 0 16 16"><circle cx="8" cy="9" r="5.5" fill="none" stroke="#fff" stroke-width="1.8"/><path d="M8 6v3l2 1" stroke="#fff" stroke-width="1.5" fill="none"/></svg>
      <svg width="20" height="14" viewBox="0 0 20 14"><path d="M0 3Q10-3 20 3L10 14Z" fill="#fff"/></svg>
      <svg width="14" height="14" viewBox="0 0 14 14"><path d="M0 14L14 0V14Z" fill="#fff"/></svg>
      <svg width="8" height="14" viewBox="0 0 8 14"><rect x="0.5" y="1.5" width="7" height="12" fill="none" stroke="#fff"/><rect x="2.5" y="0" width="3" height="2" fill="#fff"/><rect x="1.5" y="8" width="5" height="5" fill="#fff"/></svg>
      <span>16:54</span>
    </div>
    <header class="app-bar">
      <svg class="back" width="15" height="15" viewBox="0 0 15 15"><circle cx="7.5" cy="7.5" r="7.5" fill="#fff"/><path d="M9 4L5.5 7.5L9 11" stroke="#9c130f" stroke-width="2" fill="none"/></svg>
      USER INFO
      <svg class="menu" width="22" height="20" viewBox="0 0 22 20"><path d="M0 2H22M0 10H22M0 18H22" stroke="#fff" stroke-width="2.2"/></svg>
    </header>
    <h1 class="app-name"><span class="line-1">TALLYVANE</span><span class="line-2">PAIR</span></h1>
    <div class="field row-1">Country<span class="caret">▼</span></div>
    <div class="field row-2">Age Range<span class="caret">▼</span></div>
    <div class="button button--go row-3">GO!</div>
    <nav class="nav-bar">
      <svg style="left:72px" width="18" height="20" viewBox="0 0 18 20"><path d="M16 1L2 10L16 19Z" fill="none" stroke="#fff" stroke-width="1.8"/></svg>
      <svg style="left:170px" width="20" height="20" viewBox="0 0 20 20"><circle cx="10" cy="10" r="8.5" fill="none" stroke="#fff" stroke-width="1.8"/></svg>
      <svg style="left:272px" width="16" height="20" viewBox="0 0 16 20"><rect x="1" y="3" width="14" height="14" fill="none" stroke="#fff" stroke-width="1.8"/></svg>
    </nav>
  </section>

  <!-- Combo chart screen -->
  <section class="phone phone--chart">
    <div class="backdrop" role="img" aria-label="Deep red and purple glowing background with faint concentric rings"></div>
    <div class="status-bar">
      <svg width="16" height="16" viewBox="0 0 16 16"><circle cx="8" cy="9" r="5.5" fill="none" stroke="#fff" stroke-width="1.8"/><path d="M8 6v3l2 1" stroke="#fff" stroke-width="1.5" fill="none"/></svg>
      <svg width="20" height="14" viewBox="0 0 20 14"><path d="M0 3Q10-3 20 3L10 14Z" fill="#fff"/></svg>
      <svg width="14" height="14" viewBox="0 0 14 14"><path d="M0 14L14 0V14Z" fill="#fff"/></svg>
      <svg width="8" height="14" viewBox="0 0 8 14"><rect x="0.5" y="1.5" width="7" height="12" fill="none" stroke="#fff"/><rect x="2.5" y="0" width="3" height="2" fill="#fff"/><rect x="1.5" y="8" width="5" height="5" fill="#fff"/></svg>
      <span>16:54</span>
    </div>
    <header class="app-bar">
      <svg class="back" width="15" height="15" viewBox="0 0 15 15"><circle cx="7.5" cy="7.5" r="7.5" fill="#fff"/><path d="M9 4L5.5 7.5L9 11" stroke="#9c130f" stroke-width="2" fill="none"/></svg>
      TALLYVANE PAIR
      <svg class="menu" width="22" height="20" viewBox="0 0 22 20"><path d="M0 2H22M0 10H22M0 18H22" stroke="#fff" stroke-width="2.2"/></svg>
    </header>

    <svg class="chart" viewBox="0 100 360 250">
      <path d="M45 105V318" stroke="var(--axis)" stroke-width="2.5"/>
      <path d="M26 302H334" stroke="var(--axis)" stroke-width="2.5"/>
      <circle cx="104" cy="148" r="6" fill="#fff" stroke="rgba(255,200,190,0.6)" stroke-width="3"/>
      <circle cx="270" cy="256" r="6" fill="#fff" stroke="rgba(255,200,190,0.6)" stroke-width="3"/>
    </svg>
    <span class="chart-label" style="left:13px;top:102px">Huge</span>
    <span class="chart-label" style="left:16px;top:305px">None</span>
    <span class="chart-label" style="left:36px;top:325px">1X</span>
    <span class="chart-label" style="left:313px;top:325px">10X</span>
    <span class="axis-title axis-title--y">How important is it?</span>
    <span class="axis-title" style="left:77px;top:314px">How often does it need to be done?</span>

    <div class="button pick row-1">TASK</div>
    <div class="button pick pick--day row-1">DAY</div>
    <div class="button combo row-2">COMBO</div>
    <div class="button action row-3">NEW<br>COMBO</div>
    <div class="button action action--peers row-3">SEE WHAT<br>OTHERS ARE<br>DOING</div>

    <nav class="nav-bar">
      <svg style="left:72px" width="18" height="20" viewBox="0 0 18 20"><path d="M16 1L2 10L16 19Z" fill="none" stroke="#fff" stroke-width="1.8"/></svg>
      <svg style="left:170px" width="20" height="20" viewBox="0 0 20 20"><circle cx="10" cy="10" r="8.5" fill="none" stroke="#fff" stroke-width="1.8"/></svg>
      <svg style="left:272px" width="16" height="20" viewBox="0 0 16 20"><rect x="1" y="3" width="14" height="14" fill="none" stroke="#fff" stroke-width="1.8"/></svg>
    </nav>
  </section>

</div>
</body>
</html>
```